Handyman home maintenance postcard

We would like the postcard to state what we do : Painting, plumbing, electrical, flooring, carpentry, drywall, fencing, windows and more. We would also like our promotion to state : First four hours of work is only $299. Additional hours are 25% off our regular rate of $110 an hour. Rate includes two expert handymen working to complete your job.

Target Market(s)

30-75

Industry/Entity Type

Home maintenance

```html
<!DOCTYPE html>
<html lang="en">
<head>
<meta charset="utf-8">
<title>Steadfast Home Repair – Postcard</title>
<link href="https://fonts.googleapis.com/css2?family=Signika:wght@400;500;600;700&display=swap" rel="stylesheet">
<style>
:root{
  --orange:#F07A06;
  --navy:#1F3667;
  --ink:#0C0C0C;
  --white:#FFFFFF;
  --backdrop:#787878;
  --gold:#F5A623;
  --rule:#BDBDBD;
}
*{margin:0;padding:0;box-sizing:border-box}
html,body{width:1200px;height:904px;overflow:hidden}
body{background:var(--backdrop);font-family:"Signika",sans-serif;position:relative}
.card{position:absolute;width:630px;height:420px;background:var(--white);overflow:hidden}
.card--front{left:40px;top:24px}
.card--back{left:530px;top:460px}
.card-art{position:absolute;inset:0;width:630px;height:420px}
.abs{position:absolute}

.brand{display:flex;align-items:center;gap:8px}
.brand-dot{width:30px;height:30px;border-radius:50%;background:var(--orange);flex:none}
.brand-name{font-weight:600;color:var(--ink);font-size:24px;letter-spacing:-.3px;white-space:nowrap}

/* front */
.front-brand{left:26px;top:26px}
.front-copy{left:26px;top:130px;width:318px;color:var(--white)}
.headline{font-weight:700;font-size:22.5px;line-height:26px;text-transform:uppercase}
.tagline{font-weight:600;font-size:15px;margin-top:5px}
.section-title{font-weight:700;font-size:16.5px;margin-top:12px;text-transform:uppercase}
.body-text{font-size:12px;line-height:14.8px;text-align:justify;margin-top:4px}
.body-text + .body-text{margin-top:8px}

.contact{color:var(--white)}
.contact-call{display:flex;align-items:center;gap:5px;font-weight:700;font-size:14.5px;white-space:nowrap}
.contact-call .label{color:var(--gold)}
.contact-web{display:flex;align-items:center;gap:6px;font-size:12.5px;margin-top:4px;white-space:nowrap}
.front-contact{left:384px;top:362px}

/* back */
.services-title{left:26px;top:17px;color:var(--white);font-weight:700;font-size:15px;line-height:19px;text-transform:uppercase}
.service{display:flex;align-items:center;gap:5px;color:var(--white);font-weight:500;font-size:12.3px;line-height:13px}
.service svg{flex:none}
.promo{left:25px;top:237px;width:236px;height:47px;border:2px solid var(--orange);border-radius:4px;display:flex;overflow:hidden;background:var(--white)}
.promo-label{background:var(--navy);width:158px;color:var(--gold);font-weight:700;font-size:13px;line-height:15.5px;padding:6px 0 0 11px;text-transform:uppercase;letter-spacing:.2px}
.promo-price{flex:1;color:var(--navy);font-weight:600;font-size:29px;display:flex;align-items:center;justify-content:center;letter-spacing:-1px}
.rates{left:26px;top:296px;display:flex;color:var(--navy);font-weight:600;font-size:13.5px;line-height:17px}
.rates .accent{color:var(--orange)}
.rates .divider{width:1px;background:var(--navy);margin:2px 10px}
.rates-note{left:26px;top:333px;font-size:10.8px;line-height:14px;color:var(--ink);width:240px}
.back-contact{left:26px;top:373px}

.back-brand{left:345px;top:26px;gap:6px}
.back-brand .brand-dot{width:18px;height:18px}
.back-brand .brand-name{font-size:14px;letter-spacing:-.2px}
.address{left:359px;top:68px;font-size:10.8px;line-height:14px;color:var(--ink)}
.stamp-box{left:534px;top:27px;width:70px;height:65px;border:1px solid var(--rule)}
.address-line{height:1px;background:var(--rule);right:26px}
.mascot{left:268px;top:244px;width:118px;height:162px;border-radius:40px 40px 20px 20px;background:linear-gradient(180deg,#F29A2E 0 22%,#9A9A9A 22% 100%)}
</style>
</head>
<body>

<!-- Front of postcard -->
<section class="card card--front">
  <svg class="card-art" viewBox="0 0 630 420" aria-hidden="true">
    <defs>
      <linearGradient id="photoTone" x1="0" y1="0" x2="1" y2="1">
        <stop offset="0" stop-color="#E6E9EE"/>
        <stop offset=".55" stop-color="#9FB3CC"/>
        <stop offset="1" stop-color="#2F5F9E"/>
      </linearGradient>
    </defs>
    <rect x="330" y="240" width="300" height="180" fill="var(--ink)"/>
    <ellipse cx="495" cy="60" rx="260" ry="290" fill="url(#photoTone)" stroke="#fff" stroke-width="5"/>
    <circle cx="129" cy="331" r="241" fill="var(--orange)" stroke="#fff" stroke-width="5"/>
  </svg>
  <div class="abs" role="img" aria-label="Photo of a handyman in a blue cap and checked shirt repairing a water filter pipe" style="left:330px;top:0;width:300px;height:300px"></div>

  <div class="abs brand front-brand">
    <span class="brand-dot"></span>
    <span class="brand-name">Steadfast Home Repair</span>
  </div>

  <div class="abs front-copy">
    <h1 class="headline">Trusted Handyman<br>&amp; Repair Services</h1>
    <p class="tagline">Your Expert Go-To For Home Repairs.</p>
    <h2 class="section-title">Who We Are</h2>
    <p class="body-text">Steadfast Home Repair strives to be your go-to for home repairs. We have many years of experience in all facets of home repair and maintenance. Whether you are looking to repair that running toilet, replace that tired looking floor or give your home’s exterior or interior a fresh new color, we can get it done for you. On time, neatly and at a reasonable price.</p>
    <p class="body-text">Our expert craftsmen can complete all kinds of projects while treating you and your home with respect and care. We pride ourselves on doing your job properly the first time.</p>
  </div>

  <div class="abs contact front-contact">
    <div class="contact-call"><span class="label">CALL US TODAY:</span>
      <svg width="13" height="13" viewBox="0 0 16 16"><circle cx="8" cy="8" r="7" fill="none" stroke="var(--gold)" stroke-width="1.5"/><path d="M5.3 4.5l1.5-.3.8 1.8-.9.7a5 5 0 0 0 2.5 2.5l.7-.9 1.8.8-.3 1.5c-3.6.3-6.4-2.5-6.1-6.1z" fill="var(--gold)"/></svg>
      <span>7442 555 018</span></div>
    <div class="contact-web">
      <svg width="13" height="13" viewBox="0 0 16 16" fill="none" stroke="var(--gold)" stroke-width="1.3"><circle cx="8" cy="8" r="6.5"/><ellipse cx="8" cy="8" rx="3" ry="6.5"/><path d="M1.5 8h13M2.5 5h11M2.5 11h11"/></svg>
      <span>www.steadfasthomerepair.com</span></div>
  </div>
</section>

<!-- Back of postcard -->
<section class="card card--back">
  <svg class="card-art" viewBox="0 0 630 420" aria-hidden="true">
    <circle cx="64" cy="154" r="282" fill="var(--orange)"/>
    <path d="M0 262 L292 250 L292 420 L0 420 Z" fill="#fff"/>
    <path d="M0 262 C40 262 80 258 110 232 L0 232 Z" fill="var(--orange)"/>
    <rect x="0" y="367" width="358" height="53" fill="var(--ink)"/>
  </svg>

  <h2 class="abs services-title">We Provided A<br>Variety Of Handyman Services</h2>

  <div class="abs service" style="left:27px;top:61px"><svg width="33" height="33" viewBox="0 0 34 34"><circle cx="17" cy="17" r="16" fill="none" stroke="#fff" stroke-width="1.6"/><circle cx="17" cy="17" r="12.5" fill="none" stroke="#fff" stroke-width="1"/><path d="M11 23l9-9M18 11l5 5" stroke="#fff" stroke-width="1.6" fill="none"/></svg>Carpentry</div>
  <div class="abs service" style="left:133px;top:61px"><svg width="33" height="33" viewBox="0 0 34 34"><circle cx="17" cy="17" r="16" fill="none" stroke="#fff" stroke-width="1.6"/><circle cx="17" cy="17" r="12.5" fill="none" stroke="#fff" stroke-width="1"/><path d="M11 12v10M15 12v10M19 12v10M23 12v10M9 15h16M9 19h16" stroke="#fff" stroke-width="1.3" fill="none"/></svg>Fencing</div>
  <div class="abs service" style="left:230px;top:61px"><svg width="33" height="33" viewBox="0 0 34 34"><circle cx="17" cy="17" r="16" fill="none" stroke="#fff" stroke-width="1.6"/><circle cx="17" cy="17" r="12.5" fill="none" stroke="#fff" stroke-width="1"/><rect x="10" y="13" width="14" height="10" fill="none" stroke="#fff" stroke-width="1.4"/><path d="M12 13l5-4 5 4" stroke="#fff" stroke-width="1.2" fill="none"/></svg>Picture<br>Hanging</div>

  <div class="abs service" style="left:27px;top:104px"><svg width="33" height="33" viewBox="0 0 34 34"><circle cx="17" cy="17" r="16" fill="none" stroke="#fff" stroke-width="1.6"/><circle cx="17" cy="17" r="12.5" fill="none" stroke="#fff" stroke-width="1"/><rect x="11" y="11" width="12" height="12" fill="none" stroke="#fff" stroke-width="1.4"/></svg>Concrete</div>
  <div class="abs service" style="left:133px;top:104px"><svg width="33" height="33" viewBox="0 0 34 34"><circle cx="17" cy="17" r="16" fill="none" stroke="#fff" stroke-width="1.6"/><circle cx="17" cy="17" r="12.5" fill="none" stroke="#fff" stroke-width="1"/><rect x="11" y="11" width="12" height="12" fill="none" stroke="#fff" stroke-width="1.4"/><path d="M11 17l6-6M11 23l12-12M17 23l6-6" stroke="#fff" stroke-width="1.1"/></svg>Flooring</div>
  <div class="abs service" style="left:230px;top:104px"><svg width="33" height="33" viewBox="0 0 34 34"><circle cx="17" cy="17" r="16" fill="none" stroke="#fff" stroke-width="1.6"/><circle cx="17" cy="17" r="12.5" fill="none" stroke="#fff" stroke-width="1"/><path d="M12 11v6h8v6M10 11h4M18 23h4" stroke="#fff" stroke-width="1.6" fill="none"/></svg>Plumbing</div>

  <div class="abs service" style="left:27px;top:145px"><svg width="33" height="33" viewBox="0 0 34 34"><circle cx="17" cy="17" r="16" fill="none" stroke="#fff" stroke-width="1.6"/><circle cx="17" cy="17" r="12.5" fill="none" stroke="#fff" stroke-width="1"/><path d="M13 10h8M13 14h8M13 18h8M13 22h8M17 10v14" stroke="#fff" stroke-width="1.3"/></svg>Drywall</div>
  <div class="abs service" style="left:133px;top:145px"><svg width="33" height="33" viewBox="0 0 34 34"><circle cx="17" cy="17" r="16" fill="none" stroke="#fff" stroke-width="1.6"/><circle cx="17" cy="17" r="12.5" fill="none" stroke="#fff" stroke-width="1"/><rect x="11" y="10" width="12" height="5" fill="none" stroke="#fff" stroke-width="1.4"/><path d="M17 15v9" stroke="#fff" stroke-width="2"/></svg>Painting</div>
  <div class="abs service" style="left:230px;top:145px"><svg width="33" height="33" viewBox="0 0 34 34"><circle cx="17" cy="17" r="16" fill="none" stroke="#fff" stroke-width="1.6"/><circle cx="17" cy="17" r="12.5" fill="none" stroke="#fff" stroke-width="1"/><rect x="11" y="10" width="12" height="14" fill="none" stroke="#fff" stroke-width="1.4"/><path d="M17 10v14M11 17h12" stroke="#fff" stroke-width="1.2"/></svg>Windows<br>&amp; more</div>

  <div class="abs service" style="left:27px;top:188px"><svg width="33" height="33" viewBox="0 0 34 34"><circle cx="17" cy="17" r="16" fill="none" stroke="#fff" stroke-width="1.6"/><circle cx="17" cy="17" r="12.5" fill="none" stroke="#fff" stroke-width="1"/><path d="M14 10v4M20 10v4M12 14h10v3a5 5 0 0 1-10 0zM17 22v3" stroke="#fff" stroke-width="1.4" fill="none"/></svg>Electrical</div>
  <div class="abs service" style="left:133px;top:188px"><svg width="33" height="33" viewBox="0 0 34 34"><circle cx="17" cy="17" r="16" fill="none" stroke="#fff" stroke-width="1.6"/><circle cx="17" cy="17" r="12.5" fill="none" stroke="#fff" stroke-width="1"/><circle cx="17" cy="15" r="4" fill="none" stroke="#fff" stroke-width="1.4"/><path d="M10 23h14" stroke="#fff" stroke-width="1.4"/></svg>Maintenance</div>

  <div class="abs promo">
    <div class="promo-label">First Four Hours<br>Of Work Is Only</div>
    <div class="promo-price">$299</div>
  </div>

  <div class="abs rates">
    <div>Additional hours<br>are <span class="accent">25% OFF</span></div>
    <span class="divider"></span>
    <div>Our regular rate<br>of <span class="accent">$110</span> an hour</div>
  </div>
  <p class="abs rates-note">Rate includes two expert handymen working to complete your job.</p>

  <div class="abs contact back-contact">
    <div class="contact-call"><span class="label">CALL US TODAY:</span>
      <svg width="13" height="13" viewBox="0 0 16 16"><circle cx="8" cy="8" r="7" fill="none" stroke="var(--gold)" stroke-width="1.5"/><path d="M5.3 4.5l1.5-.3.8 1.8-.9.7a5 5 0 0 0 2.5 2.5l.7-.9 1.8.8-.3 1.5c-3.6.3-6.4-2.5-6.1-6.1z" fill="var(--gold)"/></svg>
      <span>7442 555 018</span></div>
    <div class="contact-web">
      <svg width="13" height="13" viewBox="0 0 16 16" fill="none" stroke="var(--gold)" stroke-width="1.3"><circle cx="8" cy="8" r="6.5"/><ellipse cx="8" cy="8" rx="3" ry="6.5"/><path d="M1.5 8h13M2.5 5h11M2.5 11h11"/></svg>
      <span>www.steadfasthomerepair.com</span></div>
  </div>

  <div class="abs mascot" role="img" aria-label="Illustrated grey cat mascot in an orange hard hat holding a hammer"></div>

  <div class="abs brand back-brand">
    <span class="brand-dot"></span>
    <span class="brand-name">Steadfast Home Repair</span>
  </div>
  <p class="abs address">4120 Harbor View Ave, #118,<br>&nbsp;Los Angeles, California, 90034</p>
  <div class="abs stamp-box"></div>
  <div class="abs address-line" style="left:385px;top:171px"></div>
  <div class="abs address-line" style="left:376px;top:215px"></div>
  <div class="abs address-line" style="left:370px;top:259px"></div>
</section>

</body>
</html>
```